Wedding filmmaker needs artistic business card design - brightwaterreels.ca

We are high end wedding filmmakers in a major market who produce cinematic wedding films. We require a business card design that communicates our quality, artistry, and professionalism yet looks progressive and friendly. Colors and design should skew appeal more to the bride-to-be who is usually the decision maker but not be overtly feminine per se. This means generally light pastel shades of ivory, purple, pink, yellow, as examples.
We already have a name logo established: the words "Brightwater Reels" in the font Great Vibes. Designs must use Tallow natural cardstock as the print stock and am leaning heavily toward our name logo in white, but I am open to black as well. Please design any color elements with spot white underneath where possible.
Do not try to compliment or take inspiration from our website design. Treat the card design as a separate stand alone.
Thank you so much for your hard work!

Target Market(s)

Affluent couples spending $50,000+ on their wedding

Industry/Entity Type

Progressive

Contact Information for Business Card

Paul Brightwater
Producer
905-418-2937
www.brightwaterreels.ca
paul@brightwaterreels.ca
social @brightwater762

Font styles to use
Serif
Sans Serif

Requirements
Must have
• - Brightwater Reels name logo (reference GIF uploaded for reference only) and catch phrase: Breathtaking wedding films (I'm open to capitalizing all three words, or just first, or all in small caps). I favor logo, and catch phrase on front of card and my contact details on the other side but if you feel strongly about a different design, go for it!
• - Design must be submitted shown on Tallow natural cardstock NOT WHITE cardstock, If you're not familiar with Tallow, this is what it looks like: http://www.quillandtwinejournal.com/wp-content/uploads/2013/07/il_570xN.837264019_kq4m.jpg
Nice to have
• - An original graphic element (eg. movie reel, bouquet, confetti, etc.) that compliments the name logo but is subtle and discreet, doesn't overpower or entangle it.
• -Great use of balance, composition, negative space, etc. I like clean tasteful design
Should not have
• -Lousy boring clip art.
• -Graphic elements, fonts, or color palette from our website
• -White cardstock background
• -designs you have previously submitted for other contests
• -Bold dark colors (eg. red, orange navy blue, etc.)
• -High tech futuristic designs like you'd create for a software company

```html
<!DOCTYPE html>
<html lang="en">
<head>
<meta charset="utf-8">
<title>Brightwater Reels – Business Card</title>
<link rel="stylesheet" href="https://fonts.googleapis.com/css2?family=Cinzel:wght@400&family=Oswald:wght@600&family=Raleway:wght@300;400&display=swap">
<style>
  :root {
    --page: #efeeec;
    --tallow: #b49a63;
    --tallow-light: #bda46d;
    --plum: #6b4a78;
    --plum-dark: #5e4069;
    --ink: #1d1a16;
    --ink-soft: #3a332a;
    --spot-white: #e6e0e8;
    --spot-white-soft: #cfc3d4;
    --reel-light: #d4d3cf;
    --reel-mid: #a9a8a4;
  }
  * { box-sizing: border-box; margin: 0; padding: 0; }
  html, body {
    width: 1200px; height: 1200px; overflow: hidden;
    background: var(--page);
  }
  .canvas { position: relative; width: 1200px; height: 1200px; }
  .card {
    position: absolute; left: 160px; width: 880px; height: 503px;
    border-radius: 3px; overflow: hidden;
    box-shadow: 0 2px 6px rgba(0,0,0,0.12);
  }

  /* ---------- Back side (contact) ---------- */
  .card-back {
    top: 67px;
    background: linear-gradient(160deg, var(--plum) 0%, var(--plum-dark) 100%);
    color: var(--spot-white);
  }
  .back-brand {
    position: absolute; left: 50px; top: 200px; width: 440px; text-align: center;
  }
  .back-brand .wordmark {
    font-family: "Cinzel", serif; font-weight: 400;
    font-size: 32px; line-height: 1.1; letter-spacing: 1px;
    color: var(--spot-white-soft); white-space: nowrap;
  }
  .back-brand .tagline {
    margin-top: 12px;
    font-family: "Cinzel", serif; font-weight: 400; font-size: 14px; letter-spacing: 2px;
    color: var(--spot-white-soft);
  }
  .contact { position: absolute; left: 540px; top: 110px; width: 320px; }
  .contact-heading {
    font-family: "Oswald", sans-serif; font-weight: 600;
    font-size: 16px; letter-spacing: 0.5px; text-transform: uppercase;
    margin-bottom: 14px; padding-left: 4px;
  }
  .contact-list { list-style: none; }
  .contact-item {
    display: flex; align-items: center; gap: 14px; margin-bottom: 12px;
    font-family: "Raleway", sans-serif; font-weight: 400;
    font-size: 16px; color: var(--spot-white);
  }
  .contact-item.phone { font-size: 29px; font-weight: 300; margin-bottom: 10px; }
  .contact-icon { width: 24px; height: 24px; flex: none; }

  /* ---------- Front side (logo) ---------- */
  .card-front {
    top: 630px;
    background: linear-gradient(170deg, var(--tallow-light) 0%, var(--tallow) 100%);
    color: var(--ink);
  }
  .front-person {
    position: absolute; top: 122px; left: 0; width: 100%; text-align: center;
    font-family: "Oswald", sans-serif; font-weight: 600; font-size: 14px;
    letter-spacing: 0.5px; text-transform: uppercase; color: var(--ink);
  }
  .front-logo {
    position: absolute; top: 160px; left: 0; width: 100%; text-align: center;
  }
  .front-logo .wordmark {
    font-family: "Cinzel", serif; font-weight: 400; font-size: 58px;
    line-height: 1.1; letter-spacing: 1px; color: var(--ink); white-space: nowrap;
  }
  .front-tagline {
    position: absolute; top: 256px; left: 0; width: 100%; text-align: center;
    font-family: "Cinzel", serif; font-weight: 400; font-size: 19px; letter-spacing: 1.5px;
    color: var(--ink-soft);
  }
  .film-reel-art {
    position: absolute; right: 0; bottom: 0; width: 260px; height: 150px;
    background: radial-gradient(ellipse at 75% 60%, var(--reel-light) 0%, var(--reel-mid) 45%, rgba(169,168,164,0) 72%);
  }
</style>
</head>
<body>
<main class="canvas">

  <section class="card card-back" aria-label="Card back, contact details">
    <div class="back-brand">
      <div class="wordmark">Brightwater Reels</div>
      <div class="tagline">BREATHTAKING WEDDING FILMS</div>
    </div>
    <div class="contact">
      <div class="contact-heading">Contact Information</div>
      <ul class="contact-list">
        <li class="contact-item phone">
          <svg class="contact-icon" viewBox="0 0 24 24" aria-hidden="true">
            <rect x="8" y="3" width="8" height="18" rx="1.5" fill="none" stroke="currentColor" stroke-width="1.6"/>
            <line x1="10.5" y1="18" x2="13.5" y2="18" stroke="currentColor" stroke-width="1.4"/>
            <path d="M4.5 8 Q2.5 12 4.5 16 M19.5 8 Q21.5 12 19.5 16" fill="none" stroke="currentColor" stroke-width="1.4"/>
          </svg>
          <span>905-418-2937</span>
        </li>
        <li class="contact-item">
          <svg class="contact-icon" viewBox="0 0 24 24" aria-hidden="true">
            <circle cx="12" cy="12" r="9" fill="none" stroke="currentColor" stroke-width="1.6"/>
            <ellipse cx="12" cy="12" rx="4" ry="9" fill="none" stroke="currentColor" stroke-width="1.3"/>
            <line x1="3" y1="12" x2="21" y2="12" stroke="currentColor" stroke-width="1.3"/>
          </svg>
          <span>www.brightwaterreels.ca</span>
        </li>
        <li class="contact-item">
          <svg class="contact-icon" viewBox="0 0 24 24" aria-hidden="true">
            <rect x="3" y="6" width="18" height="12" fill="none" stroke="currentColor" stroke-width="1.6"/>
            <path d="M3 6 L12 13 L21 6" fill="none" stroke="currentColor" stroke-width="1.4"/>
          </svg>
          <span>paul@brightwaterreels.ca</span>
        </li>
        <li class="contact-item">
          <svg class="contact-icon" viewBox="0 0 24 24" aria-hidden="true">
            <circle cx="12" cy="12" r="9" fill="currentColor"/>
          </svg>
          <span>social @brightwater762</span>
        </li>
      </ul>
    </div>
  </section>

  <section class="card card-front" aria-label="Card front, name and tagline">
    <div class="front-person">Paul Brightwater Producer</div>
    <div class="front-logo">
      <span class="wordmark">Brightwater Reels</span>
    </div>
    <div class="front-tagline">BREATHTAKING WEDDING FILMS</div>
    <div class="film-reel-art" role="img" aria-label="Silver film reel with unspooling film strip illustration"></div>
  </section>

</main>
</body>
</html>
```